Frostelle packaging design

I would like to re-design my Art work with different flavor ice cream on the containers and lids example: if the flavor is chocolate I would like to show one scoop of chocolate on the container. In the attach is one container that is an example of what I have in mind.

Target Market(s)

My products will be deliver to supermarkets and local convenient stores

Colors
f78f20
ffffff
f04a50

Requirements
Must have
• I prefer Gold around the rim of the lids and ice cream picture on top
Nice to have
• Since 2001 and going strong Or we have over a decade of experience of producing ice cream.

```html
<!DOCTYPE html>
<html lang="en">
<head>
<meta charset="utf-8">
<title>Frostelle Chocolate Ice Cream Lid</title>
<link rel="stylesheet" href="https://fonts.googleapis.com/css2?family=Lilita+One&family=Open+Sans:wght@700&family=Montserrat:wght@500;600&display=swap">
<style>
  :root {
    --canvas: #ffffff;
    --rim-outer: #e9ecee;
    --rim-inner: #f3f5f6;
    --gold-ring: #ebc06d;
    --brown-upper: #8a4430;
    --brown-lower: #5e2a1d;
    --photo-light: #8e5a4a;
    --photo-dark: #6a3a2d;
    --tag-gold: #e6b21a;
    --tag-gold-dark: #b98a10;
    --badge-red: #ec1c2a;
    --text-white: #ffffff;
    --tagline-yellow: #ffde55;
    --label-gold: #e0a630;
  }
  html, body {
    margin: 0;
    padding: 0;
    width: 1200px;
    height: 1200px;
    overflow: hidden;
    background: var(--canvas);
  }
  .lid {
    display: block;
    width: 1200px;
    height: 1200px;
  }
  .flavor-tag-text {
    font-family: "Open Sans", sans-serif;
    font-weight: 700;
    font-size: 22px;
    fill: var(--text-white);
  }
  .size-badge-text {
    font-family: "Open Sans", sans-serif;
    font-weight: 700;
    font-size: 14px;
    fill: var(--text-white);
  }
  .brand-name {
    font-family: "Lilita One", sans-serif;
    font-size: 96px;
    fill: var(--text-white);
  }
  .tagline {
    font-family: "Open Sans", sans-serif;
    font-weight: 700;
    font-size: 26px;
    fill: var(--tagline-yellow);
  }
  .product-label {
    font-family: "Montserrat", sans-serif;
    font-weight: 600;
    font-size: 22px;
    letter-spacing: 2px;
    fill: var(--label-gold);
  }
  .est-line {
    font-family: "Montserrat", sans-serif;
    font-weight: 500;
    font-size: 12px;
    letter-spacing: 0.5px;
    fill: var(--label-gold);
  }
</style>
</head>
<body>
<svg class="lid" viewBox="0 0 1200 1200" xmlns="http://www.w3.org/2000/svg">
  <defs>
    <clipPath id="lid-face">
      <circle cx="600" cy="598" r="304"/>
    </clipPath>
    <linearGradient id="photo-tone" x1="0" y1="0" x2="0" y2="1">
      <stop offset="0%" stop-color="var(--photo-light)"/>
      <stop offset="100%" stop-color="var(--photo-dark)"/>
    </linearGradient>
    <linearGradient id="tag-tone" x1="0" y1="0" x2="1" y2="0">
      <stop offset="0%" stop-color="var(--tag-gold)"/>
      <stop offset="100%" stop-color="var(--tag-gold-dark)"/>
    </linearGradient>
  </defs>

  <g class="rim">
    <circle cx="600" cy="598" r="394" fill="var(--rim-outer)"/>
    <circle cx="600" cy="598" r="372" fill="var(--rim-inner)"/>
    <circle cx="600" cy="598" r="338" fill="var(--gold-ring)"/>
  </g>

  <g class="lid-face" clip-path="url(#lid-face)">
    <rect x="290" y="290" width="620" height="308" fill="var(--brown-upper)"/>
    <rect x="290" y="598" width="620" height="320" fill="var(--brown-lower)"/>
  </g>

  <rect class="scoop-photo" role="img" aria-label="Photo of a single scoop of chocolate ice cream"
        x="410" y="334" width="384" height="284" rx="16"
        fill="url(#photo-tone)"/>

  <g class="flavor-tag" transform="rotate(-8 412 508)">
    <rect x="336" y="486" width="152" height="42" rx="4" fill="url(#tag-tone)"/>
    <path d="M352 528 L384 528 L368 549 Z" fill="var(--tag-gold-dark)"/>
    <text class="flavor-tag-text" x="412" y="515" text-anchor="middle">CHOCOLATE</text>
  </g>

  <g class="size-badge">
    <circle cx="496" cy="452" r="28" fill="var(--badge-red)"/>
    <text class="size-badge-text" x="496" y="457" text-anchor="middle" transform="rotate(-12 496 452)">500ml</text>
  </g>

  <text class="brand-name" x="600" y="708" text-anchor="middle">Frostelle</text>
  <text class="tagline" x="600" y="756" text-anchor="middle">Fresh ’n Premium</text>

  <text class="product-label" x="600" y="860" text-anchor="middle">ICE CREAM</text>
  <text class="est-line" x="600" y="880" text-anchor="middle">Est. 2011</text>
</svg>
</body>
</html>
```